Meurtre chez la Vern‘

“Vern’” is the informal nickname used inside the French police for the "Escouade Vernaleuse du Nord", an elite homicide unit. The apostrophe reflects spoken language and internal slang. The title Meurtre chez la Vern’ highlights the central irony of the novel: a murder committed inside the very place meant to investigate murders.
Summary
A woman’s body is found inside the offices of Paris’s elite homicide squad. As detectives investigate, they uncover buried cases, internal rivalries and institutional silence. The closer they get to the truth, the clearer it becomes: this crime was meant to stay hidden.
Keywords : Woman’s body, Police procedural, Murder inside the police, Elite homicide unit, Dark realism, 58 rue Bastelinou.
Size : 16 x 24 cm
Title : Meurtre chez la Vern'
Author : Lucien Maréchaux
Publisher : Editions Torvelle (at the bottom of the page)
Book

```html
<!DOCTYPE html>
<html lang="fr">
<head>
<meta charset="utf-8">
<title>Meurtre chez la Vern’ — Lucien Maréchaux</title>
<link href="https://fonts.googleapis.com/css2?family=Archivo+Black&family=Arimo:wght@500&family=Bungee&family=Alfa+Slab+One&family=Abril+Fatface&family=Bowlby+One&family=Special+Elite&family=Oswald:wght@700&family=Playfair+Display:wght@900&family=Anton&display=swap" rel="stylesheet">
<style>
  :root {
    --paper: #ffffff;
    --ink: #111111;
    --map-dark: #bcb7b0;
    --map-mid: #d6d2cc;
    --map-light: #ecebe8;
    --cream: #f3e7c9;
    --newsprint: #e4e0d6;
    --red: #c8352a;
    --mustard: #d9a92c;
    --teal: #2f8f98;
    --plum: #4a2f3d;
    --pink: #e06a9c;
    --olive: #6f7440;
    --sky: #8fb4cf;
    --photo: #bab7b3;
    --photo-light: #e2e0dd;
  }
  * { margin: 0; padding: 0; box-sizing: border-box; }
  html, body { width: 800px; height: 1200px; overflow: hidden; background: var(--paper); }
  .cover { position: relative; width: 800px; height: 1200px; background: var(--paper); overflow: hidden; }

  .city-map {
    position: absolute; left: 28px; top: 55px; width: 712px; height: 895px;
    border-radius: 48% 52% 46% 54% / 44% 46% 54% 56%;
    background: radial-gradient(ellipse at 50% 48%, var(--map-dark) 0%, var(--map-mid) 45%, var(--map-light) 68%, rgba(255,255,255,0) 80%);
  }

  .title {
    position: absolute; left: 130px; top: 208px; width: 510px;
    display: flex; flex-direction: column; align-items: center; gap: 14px;
    font-weight: normal;
  }
  .title-row { display: flex; align-items: flex-end; justify-content: center; gap: 5px; }

  .cut {
    display: flex; align-items: center; justify-content: center;
    line-height: 1; padding: 6px 8px;
    box-shadow: 2px 3px 0 rgba(0,0,0,0.18);
  }
  .row-meurtre .cut { height: 104px; min-width: 62px; font-size: 74px; }
  .row-chez .cut { height: 140px; min-width: 76px; font-size: 100px; }
  .row-vern .cut { height: 168px; min-width: 90px; font-size: 124px; }
  .row-vern .cut.mark { min-width: 40px; font-size: 96px; align-items: flex-start; padding-top: 14px; }

  .tilt-l { transform: rotate(-3deg); }
  .tilt-r { transform: rotate(3deg); }
  .drop { margin-bottom: -10px; }
  .lift { margin-bottom: 12px; }

  .on-ink     { background: var(--ink);      color: var(--cream); }
  .on-cream   { background: var(--cream);    color: var(--red); }
  .on-red     { background: var(--red);      color: var(--paper); }
  .on-mustard { background: var(--mustard);  color: var(--ink); }
  .on-teal    { background: var(--teal);     color: var(--cream); }
  .on-plum    { background: var(--plum);     color: var(--mustard); }
  .on-pink    { background: var(--pink);     color: var(--ink); }
  .on-olive   { background: var(--olive);    color: var(--paper); }
  .on-sky     { background: var(--sky);      color: var(--plum); }
  .on-news    { background: var(--newsprint);color: var(--ink); }

  .f-slab   { font-family: "Alfa Slab One", serif; }
  .f-didone { font-family: "Abril Fatface", serif; }
  .f-block  { font-family: "Bungee", sans-serif; }
  .f-round  { font-family: "Bowlby One", sans-serif; }
  .f-type   { font-family: "Special Elite", monospace; }
  .f-cond   { font-family: "Anton", sans-serif; }
  .f-grot   { font-family: "Archivo Black", sans-serif; }
  .f-play   { font-family: "Playfair Display", serif; font-weight: 900; }
  .f-oswald { font-family: "Oswald", sans-serif; font-weight: 700; }

  .photo-feet {
    width: 138px; height: 100px; margin-right: 6px; margin-bottom: 18px;
    background: linear-gradient(135deg, var(--photo-light), var(--photo));
    transform: rotate(-5deg);
  }
  .news-strip {
    width: 54px; height: 180px;
    background: linear-gradient(180deg, var(--newsprint), #bcb7ad);
    transform: rotate(2deg);
  }

  .body-outline {
    position: absolute; left: 238px; top: 772px; width: 368px; height: 78px;
  }

  .author {
    position: absolute; left: 0; top: 1026px; width: 800px; text-align: center;
    font-family: "Archivo Black", "Arial Black", sans-serif; font-size: 52px;
    color: var(--ink); line-height: 1;
  }
  .publisher {
    position: absolute; left: 0; top: 1118px; width: 800px; text-align: center;
    font-family: "Arimo", Arial, sans-serif; font-weight: 500; font-size: 12px;
    color: var(--ink); letter-spacing: 0.3px;
  }
</style>
</head>
<body>
<main class="cover">
  <div class="city-map" role="img" aria-label="Plan ancien de Paris en gravure, gris sépia, fondu en vignette"></div>

  <h1 class="title" aria-label="Meurtre chez la Vern’">
    <span class="title-row row-meurtre" aria-hidden="true">
      <span class="cut on-red f-didone tilt-r">M</span>
      <span class="cut on-news f-type lift">E</span>
      <span class="cut on-olive f-cond tilt-l">U</span>
      <span class="cut on-cream f-block drop">R</span>
      <span class="cut on-ink f-play tilt-r">T</span>
      <span class="cut on-sky f-grot">R</span>
      <span class="cut on-pink f-slab tilt-l lift">E</span>
    </span>
    <span class="title-row row-chez" aria-hidden="true">
      <span class="photo-feet" role="img" aria-label="Photo noir et blanc de pieds sous un drap avec étiquette"></span>
      <span class="cut on-mustard f-oswald tilt-l">C</span>
      <span class="cut on-plum f-didone lift">H</span>
      <span class="cut on-news f-round tilt-r">E</span>
      <span class="cut on-teal f-type drop">Z</span>
      <span class="cut on-cream f-cond tilt-l lift">L</span>
      <span class="cut on-ink f-slab tilt-r">A</span>
    </span>
    <span class="title-row row-vern" aria-hidden="true">
      <span class="cut on-teal f-play tilt-l">V</span>
      <span class="cut on-mustard f-type lift">E</span>
      <span class="news-strip" role="img" aria-label="Coupure de journal avec la tour Eiffel"></span>
      <span class="cut on-pink f-block tilt-r drop">R</span>
      <span class="cut on-ink f-oswald tilt-l">N</span>
      <span class="cut mark on-red f-didone lift">’</span>
    </span>
  </h1>

  <svg class="body-outline" viewBox="0 0 368 78" role="img" aria-label="Silhouette noire d'un corps étendu au sol">
    <path d="M14 46 C10 30 30 20 48 24 L120 14 L200 8 L300 10 L350 20 C366 28 362 44 348 46 L250 52 L170 60 L100 72 L60 64 C36 66 18 60 14 46 Z" fill="var(--ink)"/>
  </svg>

  <p class="author">LUCIEN MARÉCHAUX</p>
  <p class="publisher">EDITIONS TORVELLE</p>
</main>
</body>
</html>
```